Banner Ad Design Project

We need designs for up to three vertical, retractable banners (36 inches wide, 72 inches tall) to be displayed together at conferences and trade shows. The three banners should look good together and convey the following messages:

1) Breakthrough Investments in Energy, Food and Water

2) Real Returns from Serious Solutions to Serious Problems: High-Yield Income Funds, High-Growth Equity Funds, Special Purpose Single Investments (probably best shown in list form)

3) Doing Well by Doing Good

We are trying to attract high net worth individuals to our investment funds which are focused on funding breakthrough clean technologies in the energy, food and water sectors. Please see our website at www.tallowmere.com.

Brindle Holdings is helping make the world a better place through our team of experts who analyze different innovations to identify the most promising ideas. There are investors out there who also wish to make the world a better place. Investing their money with Brindle Holdings is a great way to make that happen.

Impactful, simple elegance is what we're after. Not too much messaging in each banner.

I have attached some images but please feel free to use others. Search "biobased industries," "sustainable foods," "sustainable energy" and the like for images to include in your work. Your unique findings are encouraged!

I have offered prizes for 1st, 2nd and 3rd place, representing each of the banners.

Target Market(s)

Investors

Industry/Entity Type

Investment

Requirements
Must have
• Elegant, simple
Should not have
• Too much messaging, too much going on, too much formatting

```html
<!DOCTYPE html>
<html lang="en">
<head>
<meta charset="utf-8">
<title>Breakthrough Investments in Energy, Food, and Water</title>
<link href="https://fonts.googleapis.com/css2?family=Yanone+Kaffeesatz:wght@400&display=swap" rel="stylesheet">
<style>
  :root {
    --page: #ffffff;
    --banner-edge: #8a8a8a;
    --banner-glow: #f2f2f2;
    --accent-green: #1f9e1f;
    --title-white: #ffffff;
  }
  html, body {
    margin: 0;
    padding: 0;
    width: 753px;
    height: 1200px;
    overflow: hidden;
    background: var(--page);
  }
  .canvas {
    position: relative;
    width: 753px;
    height: 1200px;
    background: var(--page);
  }
  .banner {
    position: absolute;
    left: 76px;
    top: 0;
    width: 600px;
    height: 1200px;
    overflow: hidden;
    background:
      radial-gradient(ellipse 330px 420px at 50% 52%, var(--banner-glow) 0%, #d6d6d6 45%, rgba(160,160,160,0) 100%),
      radial-gradient(ellipse 380px 300px at 55% 30%, #e4e4e4 0%, rgba(170,170,170,0) 100%),
      var(--banner-edge);
    font-family: 'Yanone Kaffeesatz', sans-serif;
  }
  .headline {
    position: absolute;
    left: 20px;
    top: 30px;
    margin: 0;
    padding-left: 19px;
    border-left: 9px solid var(--accent-green);
    color: var(--title-white);
    font-family: 'Yanone Kaffeesatz', sans-serif;
    font-weight: 400;
    font-size: 88px;
    line-height: 96px;
    letter-spacing: 0;
  }
  .puzzle {
    position: absolute;
    left: 0;
    top: 0;
    width: 600px;
    height: 1200px;
  }
  .brand-name {
    font-family: 'Yanone Kaffeesatz', sans-serif;
    font-weight: 400;
    font-size: 36px;
    fill: var(--title-white);
  }
</style>
</head>
<body>
<div class="canvas">
  <section class="banner">
    <h1 class="headline">Breakthrough<br>Investments in<br>Energy, Food,<br>and Water</h1>

    <svg class="puzzle" viewBox="0 0 600 1200" xmlns="http://www.w3.org/2000/svg">
      <defs>
        <linearGradient id="tone-car" x1="0" y1="0" x2="1" y2="1">
          <stop offset="0" stop-color="#f4f4f4"/>
          <stop offset="0.55" stop-color="#c3152a"/>
          <stop offset="1" stop-color="#e8e8e8"/>
        </linearGradient>
        <linearGradient id="tone-led" x1="0" y1="0" x2="1" y2="1">
          <stop offset="0" stop-color="#e9eef0"/>
          <stop offset="1" stop-color="#9aa3a6"/>
        </linearGradient>
        <linearGradient id="tone-motor" x1="0" y1="0" x2="1" y2="1">
          <stop offset="0" stop-color="#f5f5f5"/>
          <stop offset="0.5" stop-color="#2a2a2a"/>
          <stop offset="1" stop-color="#f0f0f0"/>
        </linearGradient>
        <linearGradient id="tone-solar" x1="0" y1="0" x2="1" y2="1">
          <stop offset="0" stop-color="#9fd0f0"/>
          <stop offset="1" stop-color="#1f5fc4"/>
        </linearGradient>
        <linearGradient id="tone-grass" x1="0" y1="0" x2="0" y2="1">
          <stop offset="0" stop-color="#e4f0c8"/>
          <stop offset="0.5" stop-color="#9ad11a"/>
          <stop offset="1" stop-color="#4f8f10"/>
        </linearGradient>
        <filter id="piece-shadow" x="-20%" y="-20%" width="140%" height="140%">
          <feDropShadow dx="0" dy="4" stdDeviation="6" flood-color="#000" flood-opacity="0.25"/>
        </filter>
      </defs>

      <g filter="url(#piece-shadow)">
        <polygon role="img" aria-label="Photo of a red electric car, front wheel" points="440,500 600,660 440,820 280,660" fill="url(#tone-car)"/>
        <polygon role="img" aria-label="Photo of a clear LED lamp" points="300,655 435,790 300,925 165,790" fill="url(#tone-led)"/>
        <polygon role="img" aria-label="Photo of an electric motor" points="120,715 235,830 120,945 5,830" fill="url(#tone-motor)"/>
        <polygon role="img" aria-label="Photo of solar panels under blue sky" points="260,860 390,990 260,1120 130,990" fill="url(#tone-solar)"/>
        <polygon role="img" aria-label="Photo of a green grass field" points="405,965 520,1080 405,1195 290,1080" fill="url(#tone-grass)"/>
        <polygon points="150,478 272,600 150,722 28,600" fill="var(--accent-green)"/>
      </g>

      <text class="brand-name" x="150" y="596" text-anchor="middle">Brindle</text>
      <text class="brand-name" x="150" y="630" text-anchor="middle">Holdings</text>
    </svg>
  </section>
</div>
</body>
</html>
```